Meatball Posters

We are opening a Meatball Sandwich Shop called
Orvin's Legendary Slider Shack. It is a quirky concept with a fun, casual, and sometime mildly inappropriate theme.
Sandwiches Like
"Saucy Rounds" Blue Cheese Bacon Meatball Sandwich
"Caramba" Tex Mex Meatball Sandwich
"Nonna's Last Word" Classic Meatball Sandwich
You get the idea......We are covering the interior of the place with posters of different meatball things.....That is where this comes in. I am looking for fun, quirky posters that incorporate meatballs. Think along the lines of the movie "The Curious Case of the Pancake Tower.....Think of a posted of the last supper with a giant cartoon bowl of meatballs on the table....nothing is off the table. We just need our customers to look at it and chuckle, laugh or think...
It is a fast food type place and the logo is red and yellow. I uploaded a color scheme but don't feel you are limited to just that. It is just a guide.
Target Market(s)
Blue collar workers, college kids,
Industry/Entity Type
Movie
Requirements
Must have
- It has to be fun and quirky but not too offensive or inappropriate
Nice to have
- Look at the color scheme I uploaded...I like the idea of doing it cartoon "like"
Should not have
- No Porn....abusive etc...

```html
<!DOCTYPE html>
<html lang="en">
<head>
<meta charset="utf-8">
<title>Grab the Ball by the Horns – Poster</title>
<link rel="stylesheet" href="https://fonts.googleapis.com/css2?family=Montserrat:wght@600&family=Rye&family=Uncial+Antiqua&display=swap">
<style>
  :root {
    --page: #ffffff;
    --poster-edge: #ffffff;
    --frame: #4a3a22;
    --sky-top: #b99d7b;
    --sky-mid: #a58b66;
    --field: #6d6a44;
    --field-deep: #4d4a2a;
    --ink-white: #ffffff;
    --ink-black: #111111;
    --art-light: #a5613e;
    --art-dark: #4a2a18;
  }
  * { margin: 0; padding: 0; box-sizing: border-box; }
  html, body {
    width: 1200px; height: 1000px; overflow: hidden;
    background: var(--page);
  }
  .poster {
    position: absolute; left: 255px; top: 15px;
    width: 645px; height: 970px;
    background: var(--poster-edge);
    padding: 12px;
  }
  .poster-field {
    position: relative; width: 100%; height: 100%;
    border: 3px solid var(--frame);
    overflow: hidden;
    background: linear-gradient(180deg, var(--sky-top) 0%, var(--sky-mid) 30%, var(--field) 52%, var(--field-deep) 100%);
  }
  .hero-art {
    position: absolute; left: 130px; top: 265px;
    width: 440px; height: 640px;
  }
  .headline {
    position: absolute; left: 0; width: 100%;
    text-align: center; white-space: nowrap;
  }
  .line-sans {
    font-family: "Montserrat", sans-serif; font-weight: 600;
    color: var(--ink-white); font-size: 72px;
    line-height: 1;
  }
  .line-western {
    font-family: "Rye", serif;
    color: var(--ink-white); line-height: 1;
    -webkit-text-stroke: 3px var(--ink-black);
    text-shadow: -6px 6px 0 var(--ink-black), -9px 9px 0 var(--ink-black);
  }
  .grab-the { top: 18px; letter-spacing: 12px; padding-left: 12px; }
  .ball { top: 70px; font-size: 196px; letter-spacing: 2px; }
  .by-the { top: 257px; letter-spacing: 32px; padding-left: 32px; }
  .horns { top: 318px; font-size: 146px; letter-spacing: 1px; }
  .tagline-lead {
    position: absolute; left: 45px; top: 736px;
    font-family: "Montserrat", sans-serif; font-weight: 600;
    color: var(--ink-white); font-size: 24px; letter-spacing: 1px;
    white-space: nowrap;
  }
  .sandwich-name {
    position: absolute; left: 20px; right: 20px; top: 772px;
    text-align: center; white-space: nowrap;
    font-family: "Uncial Antiqua", serif;
    color: var(--ink-white); font-size: 100px; line-height: 1.1;
  }
</style>
</head>
<body>
  <main class="poster">
    <div class="poster-field">
      <svg class="hero-art" role="img" aria-label="Illustration of a cowboy riding a giant meatball bull with long horns" viewBox="0 0 440 640">
        <defs>
          <radialGradient id="art-tone" cx="50%" cy="62%" r="55%">
            <stop offset="0%" stop-color="var(--art-light)"/>
            <stop offset="100%" stop-color="var(--art-dark)"/>
          </radialGradient>
        </defs>
        <rect x="0" y="0" width="440" height="640" rx="180" fill="url(#art-tone)" opacity="0.85"/>
      </svg>

      <div class="headline line-sans grab-the">GRAB THE</div>
      <div class="headline line-western ball">BALL</div>
      <div class="headline line-sans by-the">BY THE</div>
      <div class="headline line-western horns">HORNS</div>

      <div class="tagline-lead">GET SOME</div>
      <div class="sandwich-name">Caramba</div>
    </div>
  </main>
</body>
</html>
```